Celebrating 50 Years of Brannock

This will be a vinyl 10 foot by 8 foot large banner hung at a 50 year celebration. Attached you will find the word document that it will need to have on it and the logo and the invitation - both in all different formats - be creative as possible while staying with brand. We want a dynamic representation of the accomplishments over the last 50 years.

Target Market(s)

To use at a function to celebrate our 50th years in business

Industry/Entity Type

Hospitality

Colors

Designer to choose colors to be used in the design.

Requirements
Must have
• the attached logo and the events
Nice to have
• branding to tie into
Should not have
• should not boring and appear flat

```html
<!DOCTYPE html>
<html lang="en">
<head>
<meta charset="utf-8">
<title>Brannock Family History – 50 Years of Hospitality</title>
<link rel="stylesheet" href="https://fonts.googleapis.com/css2?family=Cinzel:wght@600;700&family=Montserrat:wght@500&family=Roboto+Condensed:wght@400&display=swap">
<style>
  :root {
    --page-bg: #d4d4d6;
    --banner-deep: #1479c4;
    --banner-mid: #1c90d8;
    --banner-glow: #35aef0;
    --ink-white: #ffffff;
    --row-light: #ffffff;
    --row-shade: #a2a4a8;
    --row-text: #1d1d1f;
    --frame: #eef2f6;
  }
  * { box-sizing: border-box; margin: 0; padding: 0; }
  html, body { width: 1200px; height: 1200px; overflow: hidden; }
  body { background: var(--page-bg); position: relative; }

  .banner {
    position: absolute; left: 20px; top: 136px;
    width: 1160px; height: 928px;
    background:
      radial-gradient(ellipse 70% 45% at 50% 18%, var(--banner-glow) 0%, rgba(53,174,240,0) 70%),
      linear-gradient(180deg, var(--banner-mid) 0%, var(--banner-deep) 100%);
    color: var(--ink-white);
  }
  .banner__title {
    position: absolute; top: 66px; left: 0; right: 0;
    text-align: center;
    font-family: "Cinzel", serif; font-weight: 700;
    font-size: 58px; letter-spacing: 0.5px; line-height: 1;
    white-space: nowrap;
  }
  .banner__title span + span { margin-left: 26px; }
  .banner__subtitle {
    position: absolute; top: 150px; left: 124px; right: 124px;
    display: flex; align-items: center; gap: 14px;
    font-family: "Montserrat", sans-serif; font-weight: 500;
    font-size: 36px; letter-spacing: 3px; white-space: nowrap;
  }
  .banner__subtitle::before, .banner__subtitle::after {
    content: ""; flex: 1; height: 1px; background: var(--ink-white);
  }

  .timeline {
    position: absolute; left: 33px; right: 33px; top: 233px; height: 654px;
    background: var(--frame); padding: 4px;
    display: grid; grid-template-columns: 357fr 420fr 393fr; gap: 8px;
  }
  .timeline__column {
    display: grid; grid-template-rows: repeat(30, 1fr); row-gap: 1px;
    list-style: none; min-width: 0;
  }
  .timeline__event {
    display: flex; align-items: center; padding-left: 4px;
    font-family: "Roboto Condensed", sans-serif; font-size: 9.2px;
    white-space: nowrap; overflow: hidden;
    background: var(--row-light); color: var(--row-text);
  }
  .timeline__event:nth-child(even) { background: var(--row-shade); color: var(--ink-white); }
  .timeline__column--narrow .timeline__event { font-size: 8.4px; }
</style>
</head>
<body>
<section class="banner">
  <h1 class="banner__title"><span>BRANNOCK</span><span>FAMILY</span><span>HISTORY</span></h1>
  <p class="banner__subtitle">50 YEARS OF HOSPITALITY</p>

  <div class="timeline">
    <ul class="timeline__column">
      <li class="timeline__event">1963 – Purchased Misty Peaks Property</li>
      <li class="timeline__event">1963 – Purchased Hickory's Barbeque Property</li>
      <li class="timeline__event">1965 – Purchased Silver Ranch Property &amp; Stonebrook Inn Property</li>
      <li class="timeline__event">1967 – Purchased Elm Hollow Property</li>
      <li class="timeline__event">1968 – Opened 1st Motel at Misty Peaks Property (22 Units)</li>
      <li class="timeline__event">1971 – Opened Misty Ridge Pancake House</li>
      <li class="timeline__event">1971 – Purchased Laurel River Court (35 Units) / Now Brookside Inn</li>
      <li class="timeline__event">1971 – Opened 2nd Building at Misty Peaks Property (20 Units)</li>
      <li class="timeline__event">1972 – Opened 3rd Building at Misty Peaks Property (39 Units)</li>
      <li class="timeline__event">1972 – Opened Copperhead Kingdom</li>
      <li class="timeline__event">1973 – Purchased Campground (10 Acres) / Now Camp Riverbend</li>
      <li class="timeline__event">1973 – Purchased Cabanas / Now Brookside Inn at Rivers Landing</li>
      <li class="timeline__event">1974 – Opened and Built Bethel Motel (20 Units)</li>
      <li class="timeline__event">1975 – Built and Added 12 Units to Misty Peaks Property</li>
      <li class="timeline__event">1976 – Built and Added Misty Ridge Pancake House to Misty Peaks Property</li>
      <li class="timeline__event">1976 – Remodeled and Opened Retail Beverage Store</li>
      <li class="timeline__event">1977 – Built and Opened World's Largest Water Slide</li>
      <li class="timeline__event">1978 – Purchased Uncle Abe's Property / The Old Hartwell Farm</li>
      <li class="timeline__event">1979 – Built and Opened Gas Station Quik Mart</li>
      <li class="timeline__event">1982 – Remodeled and Opened Uncle Abe's Pancake House</li>
      <li class="timeline__event">1982 – Built and Opened Bargain Barn</li>
      <li class="timeline__event">1986 – Construction Company Started – Brannock Construction</li>
      <li class="timeline__event">1986 – Built and Opened Stonebrook Inn (57 Units)</li>
      <li class="timeline__event">1987 – Remodeled and Added 23 Units to Misty Peaks Property</li>
      <li class="timeline__event">1988 – Built and Added 45 Units to Bethel Motel</li>
      <li class="timeline__event">1989 – Misty Ridge Resorts Brand Developed</li>
      <li class="timeline__event">1989 – Built and Opened Brookside Inn (112 Units)</li>
      <li class="timeline__event">1990 – Purchased Drive-In Theater Property</li>
      <li class="timeline__event">1990 – Remodeled and Opened Misty Ridge Pancake House</li>
      <li class="timeline__event">1990 – Misty Ridge Receptive Brand Developed</li>
    </ul>
    <ul class="timeline__column">
      <li class="timeline__event">1991 – Built and Opened Valley View Lodge / Now Parkway Inn (62 Units)</li>
      <li class="timeline__event">1991 – Built and Opened Valley View Winery</li>
      <li class="timeline__event">1992 – Built and Opened 62 Unit Addition to Valley View Lodge / Now Parkway Inn</li>
      <li class="timeline__event">1993 – Replaced Uncle Abe's Pancake House with Homestead Kitchen (#1 in the World)</li>
      <li class="timeline__event">1994 – Awarded Rising Star 50 – Ridge Metropolitan Area</li>
      <li class="timeline__event">1994 – Opened Orchard Barn Winery</li>
      <li class="timeline__event">1994 – Built and Opened Laserzone a Family Entertainment Center</li>
      <li class="timeline__event">1994 – Built and Opened Country Stay Suites (138 Units) / Now Country Falls Waterpark Resort</li>
      <li class="timeline__event">1995 – Awarded Rising Star 50 – Ridge Metropolitan Area</li>
      <li class="timeline__event">1995 – Built and Opened Brookside Inn at Rivers Landing (60 Units)</li>
      <li class="timeline__event">1995 – Built and Opened Misty Ridge Convention Center</li>
      <li class="timeline__event">1995 – Replaced Misty Ridge Pancake House with Silver Ranch Cedar Forge (#1 in the World)</li>
      <li class="timeline__event">1996 – Awarded Rising Star 50 – Ridge Metropolitan Area</li>
      <li class="timeline__event">1996 – Built and Opened Hickory's BBQ and Ribs</li>
      <li class="timeline__event">1996 – Built and Opened Summit Chemical</li>
      <li class="timeline__event">1996 – Built and Opened Silver Ranch in Hollisville</li>
      <li class="timeline__event">1996 – Purchased Senator's Landing Property</li>
      <li class="timeline__event">1996 – Opened Dairy Dip</li>
      <li class="timeline__event">1997 – Awarded Rising Star 50 – Ridge Metropolitan Area</li>
      <li class="timeline__event">1997 – Purchased Fair Air Mountain Inn / Fair Air Lodge</li>
      <li class="timeline__event">1997 – Purchased Hearthside Suites</li>
      <li class="timeline__event">1997 – Built and Opened Weekend Grill Hollisville</li>
      <li class="timeline__event">1997 – Built and Opened Mr. Tony's Pizza</li>
      <li class="timeline__event">1997 – Brannock Development Company Reorganized Into Separate Divisions</li>
      <li class="timeline__event">1998 – Awarded Rising Star 50 – Ridge Metropolitan Area</li>
      <li class="timeline__event">1998 – Opened Salty Sam's Light House Grill / Route 9 Roadhouse</li>
      <li class="timeline__event">1999 – Built Morning Donuts / Scoops Ice Cream in Hollisville</li>
      <li class="timeline__event">1999 – Awarded Tourism Leader of the Year – City of Cedar Forge</li>
      <li class="timeline__event">1999 – Built and Opened Weekend Grill Laurelburg</li>
      <li class="timeline__event">1999 – Built and Opened Stony Creek Grille</li>
    </ul>
    <ul class="timeline__column timeline__column--narrow">
      <li class="timeline__event">1999 – Built and Opened Senator's Landing Outlet Mall</li>
      <li class="timeline__event">1999 – Built and Opened Senator's Palace</li>
      <li class="timeline__event">2000 – Opened Seven Pines Steakhouse</li>
      <li class="timeline__event">2001 – Opened Morning Donuts / Scoops Ice Cream in Ridgeway</li>
      <li class="timeline__event">2001 – Built and Opened Senator's Inn</li>
      <li class="timeline__event">2001 – Built and Opened 1st Griddlecakes Pancake Cabin in Hollisville</li>
      <li class="timeline__event">2002 – Opened 2nd Griddlecakes Pancake Cabin in Laurelburg off Hwy 214</li>
      <li class="timeline__event">2004 – Opened 3rd Griddlecakes Pancake Cabin in Laurelburg off Hwy 506</li>
      <li class="timeline__event">2004 – Built and Opened The Resort at Senator's Landing Phase I</li>
      <li class="timeline__event">2005 – Opened 4th Griddlecakes Pancake Cabin in Cedar Forge</li>
      <li class="timeline__event">2005 – Built and Opened The Resort at Senator's Landing Phase II</li>
      <li class="timeline__event">2007 – Opened 5th Griddlecakes Pancake Cabin in Fenwick</li>
      <li class="timeline__event">2007 – Built and Opened The Resort at Senator's Landing Indoor Waterpark</li>
      <li class="timeline__event">2007 – Opened Hickory's BBQ in Laurelburg</li>
      <li class="timeline__event">2008 – Opened 6th Griddlecakes Pancake Cabin in Laurelburg</li>
      <li class="timeline__event">2009 – Built and Opened Hilltop Winery</li>
      <li class="timeline__event">2011 – Opened Meadowland Cellars</li>
      <li class="timeline__event">2011 – Opened Fondue Pot</li>
      <li class="timeline__event">2012 – Remodeled and Opened Hawk Springs Winery in Fenwick</li>
      <li class="timeline__event">2014 – Opened Doc Brannock Moonshine in Laurelburg</li>
      <li class="timeline__event">2015 – Remodeled and Opened Stonemill Winery at the Old Mill District</li>
      <li class="timeline__event">2015 – Opened Meadowland Cellars Tasting Room in Laurelburg</li>
      <li class="timeline__event">2015 – Replace Mr. Tony's Pizza with Buckeye Wings &amp; Grill</li>
      <li class="timeline__event">2016 – Built and Opened Griddlecakes Pelican Beach</li>
      <li class="timeline__event">2017 – Built and Opened Old Depot Pizza Pelican Beach</li>
      <li class="timeline__event">2017 – Opened Misty's Pancake House Cedar Forge</li>
      <li class="timeline__event">2017 – Built and Opened The Pinnacle Tower and Falls Waterpark at Country Falls Waterpark Resort</li>
      <li class="timeline__event">2017 – Built and Opened Mill Brook Center</li>
      <li class="timeline__event">2017 – Built and Opened Brannock Restaurant Group Office</li>
      <li class="timeline__event">2018 – Building Phase III of The Resort at Senator's Landing</li>
    </ul>
  </div>
</section>
</body>
</html>
```